Ready to be wowed! Snazzy, sassy, classy Realtor seeking Web banner for unique innovative Realtor!

Placer County Realtor need web banner re-design. Looking for classy, classic, clean design appealing to elite prospects. Previous focus was short sales now looking to gear towards listing and selling homes, remove short sale focus. Must include, license # 04729318, HR logo, phone, email, etc. check out LiaPorter.com for reference info. I am open to suggestions for other needed content for THE BEST WEB BANNER ON EARTH! LOL. I really want to appeal to the upscale clients, also will be getting away from orange colors going more to a green. Please contact me at LiaPorterSells@mailvista.com for more info
measurements of banner; Images of exactly 960 × 120 pixels will be used as-is. It's Wordpress Genesis.
Updates

I'm really looking for something clean that looks upscale and luxury, classy. 

Please update email address to lia@liaporter.com

Reason: I still haven't gotten what I want. I noticed some really good designs closer to the end here, I'm hoping to allow those folks and maybe a few new ones the opportunity to give me exactly what I want! Thanks!

Reason: I still don't have what I want. I want a simple design that shows that I am a Realtor, maybe a picture of a house???? or something related to real estate. Less emphasis on the Halverson Realty logo. Classy and upscale. Fonts should be easy to read but not so simply boring. Please, please, please read the brief!! I REALLY want a good banner!!

Please take a look at the site color adjustment. That's what color it will stay. www.LiaPorter.com

Reason: I'm ready to move this to the end now. I need a design. I'm extending hopefully only this last time to take a vote on them. I will be reaching out to a few select designers to make a few modifications. I appreciate everyone's time on this as you know this is a very tough and important decision to make.

Reason: Need more input

Reason: still trying to decide

Target Market(s)

upscale home sellers

Industry/Entity Type

Realtor

Requirements
Must have
• License # 04729318
Phone (555)304-2871
HR LOGO (attached)
areas of service- Roseville, Rocklin, Granite Bay
LiaPorterSells@mailvista.com

```html
<!DOCTYPE html>
<html lang="en">
<head>
<meta charset="utf-8">
<title>Lia Porter – Realtor Banner</title>
<link href="https://fonts.googleapis.com/css2?family=Freckle+Face&family=Amatic+SC:wght@700&family=Quicksand:wght@400&family=Open+Sans:wght@700&display=swap" rel="stylesheet">
<style>
  :root {
    --bg-light: #e6e6e6;
    --bg-white: #fafafa;
    --bg-dark: #2a2a2a;
    --name-green: #4f8d1f;
    --area-green: #6b9c2c;
    --contact-lime: #cddc4c;
    --ink: #141414;
    --brand-blue: #1f3f8f;
    --photo-warm: #c9a27a;
    --photo-cool: #8fa6b8;
  }
  html, body {
    margin: 0;
    padding: 0;
    overflow: hidden;
    background: #ffffff;
  }
  .banner {
    position: relative;
    width: 1200px;
    height: 150px;
    overflow: hidden;
    background:
      radial-gradient(ellipse 230px 95px at 760px 62px, rgba(30,30,30,0.95) 0%, rgba(40,40,40,0.75) 45%, rgba(255,255,255,0) 100%),
      linear-gradient(90deg, var(--bg-light) 0%, #d2d2d2 30%, var(--bg-white) 55%, #efefef 80%, #dcdcdc 100%);
  }
  .agent-photo {
    position: absolute;
    left: 0;
    top: 0;
    width: 175px;
    height: 150px;
    background: linear-gradient(160deg, var(--photo-cool) 0%, var(--photo-warm) 60%, #a37d57 100%);
  }
  .agent-name {
    position: absolute;
    left: 178px;
    top: 22px;
    margin: 0;
    font-family: "Freckle Face", cursive;
    font-weight: 400;
    font-size: 72px;
    line-height: 1;
    color: var(--name-green);
    text-shadow: 2px 2px 0 var(--ink), -1px -1px 0 var(--ink), 1px -1px 0 var(--ink), -1px 1px 0 var(--ink);
    white-space: nowrap;
  }
  .license {
    position: absolute;
    left: 206px;
    top: 120px;
    margin: 0;
    font-family: "Amatic SC", sans-serif;
    font-size: 27px;
    line-height: 1;
    color: var(--ink);
    letter-spacing: 0.5px;
  }
  .service-area {
    position: absolute;
    left: 460px;
    width: 600px;
    top: 8px;
    margin: 0;
    text-align: center;
    font-family: "Quicksand", sans-serif;
    font-size: 26px;
    line-height: 1.2;
    color: var(--area-green);
  }
  .contact {
    position: absolute;
    left: 560px;
    width: 372px;
    top: 74px;
    margin: 0;
    text-align: center;
    font-family: "Amatic SC", sans-serif;
    font-size: 30px;
    line-height: 1;
    color: var(--contact-lime);
    font-style: normal;
    letter-spacing: 0.5px;
  }
  .contact span {
    display: block;
    margin-bottom: 6px;
  }
  .brokerage {
    position: absolute;
    left: 1028px;
    top: 82px;
    width: 166px;
    height: 52px;
    display: flex;
    align-items: center;
    gap: 8px;
  }
  .brokerage-mark {
    width: 22px;
    height: 22px;
    flex: none;
    background: var(--brand-blue);
  }
  .brokerage-name {
    font-family: "Open Sans", sans-serif;
    font-weight: 700;
    font-size: 16px;
    line-height: 1.1;
    color: var(--brand-blue);
  }
</style>
</head>
<body>
  <header class="banner">
    <div class="agent-photo" role="img" aria-label="Portrait photo of the realtor"></div>
    <h1 class="agent-name">Lia Porter</h1>
    <p class="license">LICENSE# 04729318</p>
    <p class="service-area">Serving Roseville, Rocklin, Granite Bay</p>
    <address class="contact">
      <span class="contact-phone">555.304.2871</span>
      <span class="contact-email">LIAPORTERSELLS@MAILVISTA.COM</span>
    </address>
    <div class="brokerage">
      <div class="brokerage-mark"></div>
      <div class="brokerage-name">Halverson Realty</div>
    </div>
  </header>
</body>
</html>
```